Weihnachtskarte für Bikegeschäft
super arbeit. einfach, ohne grossen schnickschnack.
Zielgruppe
wir sind das bikegeschäft in st. moritz und dem oberengadin in der schweiz. wir sind auf high end kunden spezialisiert und bieten verkauf, vermietung und service. wir sind grovantix und tessavoni händler und unsere geschäftsfarben sind gelb schwarz.
Aufgabenstellung
sicher unsere mitarbeiter sollten auf dem flyer sein. statt schwarz gelb kann für die weihnachtskarte auch gold schwarz gebrauchen oder eine eigene idee. ich bin da offen. wenn fotos von st. moritz gefragt sind kann ich diese nachliefern.
Text sollte sein:
FRÖHLICHE WEIHNACHTEN
Vielen Dank für Deine Treue und das Vertrauen, das Du uns entgegenbringst! Wir sind auch über Weihnachten und Neujahr für Dich da – mit spannenden Events wie Radfahren auf Schnee und vielem mehr. Natürlich sind wir wie gewohnt 365 Tage im Jahr für Dich geöffnet. Wir wünschen dir und deinen Liebsten ein schönes Weihnachtsfest und einen guten Rutsch ins neue Jahr.
Dein Team von FENDAmora St. Moritz

```html
<!DOCTYPE html>
<html lang="de">
<head>
<meta charset="utf-8">
<title>Weihnachtskarte – FENDAmora St. Moritz</title>
<link rel="stylesheet" href="https://fonts.googleapis.com/css2?family=Playfair+Display:wght@500;600&family=Kalam:wght@400&family=Parisienne&display=swap">
<style>
  :root{
    --night:#1b1916;
    --gold:#f4b642;
    --gold-soft:#f2b53f;
    --ring-light:#3a3a3a;
    --ring-dark:#121212;
    --band:rgba(40,36,30,.72);
  }
  *{margin:0;padding:0;box-sizing:border-box}
  html,body{width:844px;height:1200px;overflow:hidden;background:var(--night)}
  .card{position:relative;width:844px;height:1200px;background:var(--night);overflow:hidden}
  .backdrop{position:absolute;inset:0}
  .town-photo{
    position:absolute;left:0;top:740px;width:844px;height:460px;
    background:linear-gradient(180deg,rgba(27,25,22,0) 0%,#2a2a30 22%,#3d3a36 45%,#6a5435 62%,#5a4a38 78%,#4a4540 100%);
  }
  .title{
    position:absolute;left:0;width:844px;text-align:center;
    font-family:"Playfair Display",serif;font-weight:500;color:var(--gold);
    text-shadow:-5px 3px 0 #000;letter-spacing:1px;line-height:1;
  }
  .title--top{top:104px;font-size:66px}
  .title--bottom{top:176px;font-size:74px;left:4px}
  .brand{
    position:absolute;top:300px;left:0;width:844px;
    display:flex;justify-content:center;align-items:center;gap:12px;
    font-family:"Kalam",cursive;font-size:30px;color:var(--gold);letter-spacing:2px;
  }
  .brand-dot{width:18px;height:18px;border-radius:50%;background:var(--gold)}
  .portrait{position:absolute;width:172px;height:172px;border-radius:50%;
    background:radial-gradient(circle at 30% 25%,var(--ring-light),var(--ring-dark) 75%);
    box-shadow:0 4px 14px rgba(0,0,0,.5)}
  .portrait-photo{position:absolute;left:18px;top:18px;width:136px;height:136px;border-radius:50%;
    background:linear-gradient(135deg,#3b3b3b 0%,#1d1d1d 55%,#0d0d0d 100%)}
  .p1{left:108px;top:349px}.p2{left:557px;top:349px}
  .p3{left:26px;top:555px}.p4{left:639px;top:555px}
  .p5{left:87px;top:762px}.p6{left:579px;top:762px}
  .thanks{
    position:absolute;left:0;width:832px;top:422px;text-align:center;
    font-family:"Parisienne",cursive;font-size:40px;color:var(--gold);
  }
  .message{
    position:absolute;left:0;width:832px;text-align:center;
    font-family:"Kalam",cursive;font-size:22px;line-height:24.5px;letter-spacing:2.2px;color:var(--gold);
  }
  .m1{top:484px}.m2{top:582px}.m3{top:728px}.m4{top:826px}
  .signoff-band{position:absolute;left:0;top:1052px;width:844px;height:105px;background:var(--band)}
  .signoff{
    position:absolute;left:0;width:844px;top:1064px;text-align:center;
    font-family:"Playfair Display",serif;font-weight:600;font-size:40px;line-height:43px;color:var(--gold);
  }
</style>
</head>
<body>
<main class="card">
  <svg class="backdrop" width="844" height="1200" viewBox="0 0 844 1200" aria-hidden="true">
    <path d="M52 0 C300 30 560 150 690 330 C790 470 830 620 844 780 L844 0 Z" fill="var(--gold)"/>
  </svg>
  <div class="town-photo" role="img" aria-label="Nachtansicht von St. Moritz mit beleuchteten Häusern im Schnee"></div>

  <h1>
    <span class="title title--top">FRÖHLICHE</span>
    <span class="title title--bottom">WEIHNACHTEN</span>
  </h1>

  <div class="brand"><span class="brand-dot"></span>FENDAmora</div>

  <div class="portrait p1"><div class="portrait-photo" role="img" aria-label="Porträt Teammitglied"></div></div>
  <div class="portrait p2"><div class="portrait-photo" role="img" aria-label="Porträt Teammitglied"></div></div>
  <div class="portrait p3"><div class="portrait-photo" role="img" aria-label="Porträt Teammitglied"></div></div>
  <div class="portrait p4"><div class="portrait-photo" role="img" aria-label="Porträt Teammitglied"></div></div>
  <div class="portrait p5"><div class="portrait-photo" role="img" aria-label="Porträt Teammitglied"></div></div>
  <div class="portrait p6"><div class="portrait-photo" role="img" aria-label="Porträt Teammitglied"></div></div>

  <p class="thanks">Vielen Dank</p>
  <p class="message m1">für Deine Treue und das<br>Vertrauen, das Du uns<br>entgegenbringst</p>
  <p class="message m2">Wir sind auch über<br>Weihnachten und Neujahr für<br>Dich da – mit spannenden<br>Events wie Radfahren auf Schnee<br>und vielem mehr</p>
  <p class="message m3">Natürlich sind wir wie gewohnt<br>365 Tage im Jahr für Dich<br>geöffnet.</p>
  <p class="message m4">Wir wünschen dir und<br>deinen Liebsten ein<br>schönes Weihnachtsfest<br>und einen guten<br>Rutsch ins neue<br>Jahr</p>

  <div class="signoff-band"></div>
  <p class="signoff">Dein Team von FENDAmora St.<br>Moritz</p>
</main>
</body>
</html>
```